British Columbia Day banner showcasing 20% off site

Banner graphic promoting our BC Day sale
Size: 1800 x 1000
- flag has been uploaded for inspiration
- examples from other companies and their sale banners have been uploaded for inspiration.
- product images can be found at www.mygreenleafhub.com, please use a variety of different products in this banner

Target Market(s)

19+

Industry/Entity Type

Cannabis

Requirements
Must have
• Phrases:
- “Celebrate BC Day with BC bud and companies”
- “20% off site wide sale*"
- Underneath phrase the date of sale “July 30th - August 3rd”
- In tiny print “*excludes all sale and bundled items”
- MUST BE 1800 X1000
Nice to have
• - images of the products or bud we carry which can be found at www.mygreenleafhub.com
- bold
Should not have
• - company logo

```html
<!DOCTYPE html>
<html lang="en">
<head>
<meta charset="utf-8">
<title>BC Day Sale Banner</title>
<link href="https://fonts.googleapis.com/css2?family=Josefin+Sans:wght@300;400&display=swap" rel="stylesheet">
<style>
  :root {
    --green: #46ad5f;
    --green-light: #8fd3a0;
    --ink: #3a3a3a;
    --paper: #ffffff;
    --sky: #a9d9e6;
    --field: #c9a35a;
    --field-deep: #9a7636;
  }
  * { margin: 0; padding: 0; box-sizing: border-box; }
  html, body { width: 1200px; height: 667px; overflow: hidden; background: var(--paper); }
  .banner {
    position: relative;
    width: 1200px;
    height: 667px;
    overflow: hidden;
    background: var(--paper);
    font-family: "Josefin Sans", sans-serif;
    color: var(--ink);
  }
  .shapes { position: absolute; inset: 0; }
  .line {
    position: absolute;
    left: 32px;
    white-space: nowrap;
    line-height: 1;
    font-weight: 400;
  }
  .headline { top: 215px; font-size: 39px; letter-spacing: 0.6px; }
  .subhead  { top: 264px; font-size: 30px; }
  .offer    { top: 318px; font-size: 43px; color: var(--green); letter-spacing: 0.4px; }
  .dates    { top: 381px; left: 34px; font-size: 26px; color: var(--green); }
  .fine-print { top: 424px; left: 31px; font-size: 15px; letter-spacing: 0.3px; }
</style>
</head>
<body>
  <div class="banner">
    <svg class="shapes" width="1200" height="667" viewBox="0 0 1200 667">
      <defs>
        <linearGradient id="photoTone" x1="0" y1="0" x2="0" y2="1">
          <stop offset="0" stop-color="#a9d9e6"/>
          <stop offset="0.42" stop-color="#d9e6d3"/>
          <stop offset="0.55" stop-color="#c9a35a"/>
          <stop offset="1" stop-color="#9a7636"/>
        </linearGradient>
        <radialGradient id="productTone" cx="0.5" cy="0.55" r="0.55">
          <stop offset="0" stop-color="#f2c9b8"/>
          <stop offset="0.55" stop-color="#f7e6dc"/>
          <stop offset="1" stop-color="#ffffff"/>
        </radialGradient>
      </defs>

      <polygon class="band" points="855,0 1200,0 1200,667 533,667" fill="var(--green)"/>
      <polygon class="band-accent" points="945,39 1200,39 1200,59 935,59 633,667 620,667" fill="var(--green-light)" opacity="0.7"/>
      <polygon class="photo" role="img" aria-label="Photo of a girl running through a golden field holding an orange pinwheel"
        points="955,59 1200,59 1200,667 645,667" fill="url(#photoTone)"/>

      <circle class="product-ring" cx="475" cy="560" r="168" fill="var(--paper)" stroke="var(--green)" stroke-width="13"/>
      <circle class="product-shot" role="img" aria-label="Stack of colourful fruit-flavoured edible packages with gummy cubes"
        cx="475" cy="560" r="161" fill="url(#productTone)"/>

      <rect class="base-strip" x="0" y="652" width="1200" height="15" fill="var(--green)"/>
    </svg>

    <h1 class="line headline">Celebrate BC Day with</h1>
    <p class="line subhead">BC bud &amp; companies</p>
    <p class="line offer">20% off site wide sale</p>
    <p class="line dates">July 30th - August 3rd</p>
    <p class="line fine-print">*Excludes all sale and bundled items</p>
  </div>
</body>
</html>
```